Web design for Crowdfunding site HopeWingsHub.com

We need a web design for christian crowdfunding website. Here is the challenge: We need responsive layout that is targeted first in iPad size of screen. It should also scale somehow down to iPhone size of screens. Web layout can be about the same size as iPad screen.

Screens should work so that main page scrolls not but only certain part of the screen scrolls and always one "page" at time. We can implement these "scrolls" then later with javascript but now we need only design. The challenge is to create this kind of hybrid website / app look.

Target is at first to raise funds to orphan people needing about $40 per month for their living and education. There is always some organization which takes care of these kids. Later there will be other christian missions included. At first we are looking to find monthly supporters.

You can be as creative as you want :) As you see from the look and feel sector, I am not looking any same traditional look which many "help kids" sites have. I am looking to reach now younger generation and therefore iPad and mobile are the main screen sizes.

Inspirational designs:
- https://examplegallery.test/profiles/studiokavrel/designs/381264?from=%2Fbrowse%2Fxhr%2Fdesigns%3Fcategory%3Dmobile-app-design
- http://www.pixelforum.test/design/8264190 Clear, simple visuals
- http://www.pixelforum.test/design/7421953 Header
- http://www.pixelforum.test/design/6392017 Contrast in the colors, i think is powerfull

Some terms could be: Kids play, kids are learning (in the school). No static posture but living like kids are. I wonder also how we could also add little bit gaming style even though the question is of reali life of real people. Giving should be rewarding.

Target Market(s)

People who want help other people.

Industry/Entity Type

Christian

Number of Pages Required

4 page

Requirements
Must have
• Homepage. Mission page (In my wireframes it was one kid).
Nice to have
• Other pages and some idea how to scroll. 4 pages is no must. If you feel easy, please give first some draft and I give comments on that.

```html
<!DOCTYPE html>
<html lang="en">
<head>
<meta charset="utf-8">
<title>HopeWingsHub – Home</title>
<link rel="stylesheet" href="https://fonts.googleapis.com/css2?family=Quicksand:wght@500;700&family=Raleway:wght@500&family=Montserrat:wght@700&display=swap">
<style>
  :root {
    --orange: #fba60f;
    --black: #000000;
    --white: #ffffff;
    --cream: #fbe9d6;
    --hero-top: #f7cfa8;
    --hero-mid: #ec9558;
    --hero-low: #c4532a;
  }
  * { box-sizing: border-box; margin: 0; padding: 0; }
  html, body { width: 1200px; height: 900px; overflow: hidden; background: var(--black); }
  body { position: relative; font-family: "Quicksand", sans-serif; color: var(--white); }

  /* Sidebar */
  .sidebar { position: absolute; left: 0; top: 0; width: 314px; height: 900px; background: var(--orange); }
  .profile { position: absolute; top: 0; left: 0; width: 314px; height: 218px; background: var(--black); }
  .profile-avatar { position: absolute; left: 77px; top: 17px; width: 141px; height: 134px; border-radius: 50%;
    border: 4px solid var(--white);
    background: radial-gradient(circle at 50% 38%, #c79a7e 0 18%, #5d6f86 40%, #2b3139 80%); }
  .status-dot { position: absolute; left: 166px; top: 11px; width: 40px; height: 40px; border-radius: 50%; background: var(--orange); }
  .profile-name { position: absolute; top: 160px; width: 100%; padding-right: 20px; text-align: center; font-size: 30px; font-weight: 500; letter-spacing: 1.5px; }

  .power-band { position: absolute; top: 218px; left: 0; width: 314px; height: 67px; display: flex; align-items: center; justify-content: center; }
  .nav { position: absolute; top: 285px; left: 0; width: 314px; list-style: none; }
  .nav-item { position: relative; height: 62px; font-size: 31px; font-weight: 500; letter-spacing: 2px; }
  .nav-item svg { position: absolute; left: 34px; top: 9px; width: 44px; height: 44px; }
  .nav-item span { position: absolute; top: 10px; line-height: 40px; }
  .nav-item.is-active { background: var(--black); height: 58px; }
  .nav-item.is-active + .nav-item { margin-top: 3px; }

  .recent-title { position: absolute; top: 643px; left: 0; width: 314px; height: 67px; background: var(--black);
    display: flex; align-items: center; justify-content: center; padding-right: 10px; font-size: 30px; font-weight: 500; letter-spacing: 1.5px; }
  .recent-list { position: absolute; top: 748px; left: 10px; display: flex; gap: 12px; }
  .recent-card { width: 90px; text-align: center; }
  .recent-thumb { width: 90px; height: 92px; border-radius: 9px; border: 2px solid #f2f2f2; }
  .recent-caption { margin-top: 5px; font-size: 11px; line-height: 11px; color: var(--black); font-weight: 500; }

  /* Hero */
  .hero { position: absolute; left: 314px; top: 0; width: 886px; height: 337px;
    background: radial-gradient(ellipse 30% 55% at 68% 45%, #d9643a 0%, rgba(217,100,58,0) 100%),
                radial-gradient(ellipse 50% 60% at 20% 30%, #fbe0c2 0%, rgba(251,224,194,0) 100%),
                linear-gradient(180deg, var(--hero-top) 0%, var(--hero-mid) 60%, var(--hero-low) 100%); }
  .hero-title { position: absolute; left: 506px; top: 202px; width: 540px; text-align: center; white-space: nowrap;
    font-family: "Montserrat", sans-serif; font-size: 26px; font-weight: 700; letter-spacing: 0.8px; color: var(--cream);
    text-shadow: 0 2px 4px rgba(0,0,0,.6); }
  .pager { position: absolute; left: 1145px; top: 168px; display: flex; flex-direction: column; gap: 14px; }
  .pager span { width: 13px; height: 13px; border-radius: 50%; background: var(--white); }

  .project-bar { position: absolute; left: 441px; top: 266px; width: 633px; height: 116px; border-radius: 58px; overflow: hidden;
    background: linear-gradient(180deg, var(--black) 0 61%, var(--orange) 61% 100%); }
  .owner-avatar { position: absolute; left: 690px; top: 254px; width: 136px; height: 136px; border-radius: 50%;
    background: var(--black); padding: 8px; }
  .owner-avatar div { width: 100%; height: 100%; border-radius: 50%; border: 2px solid var(--white);
    background: radial-gradient(circle at 50% 45%, #e7b08f 0 25%, #a64f2c 55%, #5a2414 90%); }
  .support-btn { position: absolute; left: 481px; top: 282px; width: 50px; height: 44px; border-radius: 10px;
    background: var(--orange); border: 3px solid var(--white); display: flex; align-items: center; justify-content: center; }
  .support-count { position: absolute; left: 540px; top: 291px; font-size: 20px; font-weight: 700; letter-spacing: 1px; }
  .like-icon { position: absolute; left: 587px; top: 288px; }
  .comment-bubble { position: absolute; left: 630px; top: 284px; }
  .share-list { position: absolute; left: 836px; top: 286px; display: flex; gap: 11px; list-style: none; }
  .share-btn { width: 41px; height: 41px; border-radius: 50%; background: var(--orange); border: 3px solid var(--white);
    display: flex; align-items: center; justify-content: center; font-size: 9px; font-weight: 700; color: var(--black); }

  .intro { position: absolute; left: 330px; top: 406px; width: 854px; text-align: center; white-space: nowrap;
    font-family: "Raleway", sans-serif; font-size: 17.5px; line-height: 23px; font-weight: 500; }

  /* Project grid */
  .project-grid { position: absolute; left: 314px; top: 495px; width: 886px; height: 405px;
    display: grid; grid-template-columns: 292px 296px 298px; grid-template-rows: 147px 68px 190px; }
  .project-photo { position: relative; }
  .project-label { background: var(--black); display: flex; align-items: center; justify-content: center;
    font-size: 21px; font-weight: 500; letter-spacing: 1.5px; }
  .project-label + .project-label { border-left: 1px solid #222; }
  .badge { position: absolute; right: 2px; top: 3px; height: 48px; padding: 4px; border-radius: 24px; background: var(--white); }
  .badge span { display: flex; align-items: center; gap: 3px; height: 40px; padding: 0 12px; border-radius: 20px;
    background: var(--orange); font-size: 20px; font-weight: 500; letter-spacing: 1px; }
</style>
</head>
<body>

<aside class="sidebar">
  <div class="profile">
    <div class="profile-avatar" role="img" aria-label="Profile photo of the signed-in user"></div>
    <div class="status-dot"></div>
    <div class="profile-name">Leo Marsh</div>
  </div>

  <div class="power-band">
    <svg width="40" height="40" viewBox="0 0 40 40" fill="none" stroke="#fff" stroke-width="4" stroke-linecap="round">
      <path d="M12 9a15 15 0 1 0 16 0"/><path d="M20 3v16"/>
    </svg>
  </div>

  <ul class="nav">
    <li class="nav-item is-active">
      <svg viewBox="0 0 44 44" fill="#fff"><path d="M22 4 2 21l3 3 4-3.4V40h11V29h4v11h11V20.6l4 3.4 3-3z"/></svg>
      <span style="left:112px;top:8px">Home</span>
    </li>
    <li class="nav-item">
      <svg viewBox="0 0 44 44" fill="none" stroke="#fff" stroke-width="2.6" stroke-linecap="round" stroke-linejoin="round">
        <rect x="4" y="4" width="32" height="36" rx="6"/><path d="M9 13l3 3 5-5M21 13h10M9 22l3 3 5-5M21 22h8M9 31l3 3 5-5"/>
        <path d="M33 43s-9-5-9-10a4 4 0 0 1 9-2 4 4 0 0 1 9 2c0 5-9 10-9 10z" fill="#fba60f"/>
      </svg>
      <span style="left:92px">Missions</span>
    </li>
    <li class="nav-item">
      <svg viewBox="0 0 44 44" fill="#fff"><path d="M22 4 13 24l8-1-3 17 12-22-8 1z"/></svg>
      <span style="left:98px">Popular</span>
    </li>
    <li class="nav-item">
      <svg viewBox="0 0 44 44" fill="none" stroke="#fff" stroke-width="3.5"><circle cx="22" cy="22" r="18"/><path d="M22 19v13" stroke-linecap="round"/><circle cx="22" cy="13" r="1.5" fill="#fff"/></svg>
      <span style="left:110px">About</span>
    </li>
    <li class="nav-item">
      <svg viewBox="0 0 44 44" fill="#fff"><path d="M19 2h6l1 6 4 2 5-4 4 4-4 5 2 4 6 1v6l-6 1-2 4 4 5-4 4-5-4-4 2-1 6h-6l-1-6-4-2-5 4-4-4 4-5-2-4-6-1v-6l6-1 2-4-4-5 4-4 5 4 4-2zM22 14a8 8 0 1 0 0 16 8 8 0 0 0 0-16z"/></svg>
      <span style="left:94px">Settings</span>
    </li>
  </ul>

  <div class="recent-title">Recent Missions</div>
  <div class="recent-list">
    <div class="recent-card">
      <div class="recent-thumb" role="img" aria-label="Mission photo: girl standing with a horse in a misty field" style="background:linear-gradient(180deg,#c9d3d6 0,#aab3b2 55%,#6a5a4c 100%)"></div>
      <p class="recent-caption">Small text<br>about...</p>
    </div>
    <div class="recent-card">
      <div class="recent-thumb" role="img" aria-label="Mission photo: horse portrait in golden light" style="background:linear-gradient(160deg,#f4e2b8 0,#d7a96b 50%,#8a5a2e 100%)"></div>
      <p class="recent-caption">Small text<br>about...</p>
    </div>
    <div class="recent-card">
      <div class="recent-thumb" role="img" aria-label="Mission photo: swimmer under clear sea water" style="background:linear-gradient(180deg,#9ad8f0 0,#3fb0d8 40%,#1a7aa6 100%)"></div>
      <p class="recent-caption">Small text<br>about...</p>
    </div>
  </div>
</aside>

<section class="hero" role="img" aria-label="Featured project photo: woman with arms open against a warm sunset sky"></section>
<h1 class="hero-title">THE NORA BELDEN WATER PROJECT</h1>
<div class="pager"><span></span><span></span><span></span></div>

<div class="project-bar"></div>
<div class="support-btn">
  <svg width="22" height="22" viewBox="0 0 22 22"><path d="M8 1h6v7h7v6h-7v7H8v-7H1V8h7z" fill="#000"/></svg>
</div>
<div class="support-count">134</div>
<svg class="like-icon" width="32" height="30" viewBox="0 0 32 30" fill="none" stroke="#fff" stroke-width="3">
  <path d="M16 27S3 19 3 10a7 7 0 0 1 13-3 7 7 0 0 1 13 3c0 9-13 17-13 17z"/>
</svg>
<svg class="comment-bubble" width="56" height="40" viewBox="0 0 56 40">
  <path d="M20 3h16a17 15 0 0 1 0 30h-2l8 5-16-5h-6a17 15 0 0 1 0-30z" fill="#fba60f" stroke="#fff" stroke-width="3"/>
  <text x="28" y="23" text-anchor="middle" font-family="Quicksand, sans-serif" font-size="11" font-weight="700" font-style="italic" fill="#000">200</text>
</svg>
<div class="owner-avatar" role="img" aria-label="Portrait of the project owner"><div></div></div>
<ul class="share-list" aria-label="Share">
  <li class="share-btn">Kivo</li><li class="share-btn">Pola</li><li class="share-btn">Nubo</li><li class="share-btn">Temi</li>
</ul>

<p class="intro">Lorem ipsum dolor sit amet, consectetur adipisicing elit, sed do eiusmod tempor incididunt<br>ut labore et dolore magna aliqua. Ut enim ad mis aute irure dolor in reprehenderit in<br>voluptate velit esse cillum dolore eu fugiat nulla pariatur. Excepteur sint occaecat</p>

<main class="project-grid">
  <div class="project-photo" role="img" aria-label="Project photo: woman praying in warm light" style="background:linear-gradient(110deg,#3e2614 0,#8a5f34 35%,#d6b27a 65%,#efdcae 100%)">
    <div class="badge"><span><svg width="18" height="18" viewBox="0 0 22 22"><path d="M8 1h6v7h7v6h-7v7H8v-7H1V8h7z" fill="#000"/></svg>134</span></div>
  </div>
  <div class="project-photo" role="img" aria-label="Project photo: bright sun over a teal sea with a bird" style="background:radial-gradient(ellipse 45% 55% at 48% 35%,#f2fdff 0,#8fd0dc 30%,#2d7888 65%,#143e4c 100%)">
    <div class="badge"><span><svg width="18" height="18" viewBox="0 0 22 22"><path d="M8 1h6v7h7v6h-7v7H8v-7H1V8h7z" fill="#000"/></svg>134</span></div>
  </div>
  <div class="project-photo" role="img" aria-label="Project photo: two smiling children outdoors" style="background:linear-gradient(90deg,#5a4232 0,#8e6c52 30%,#b8a58c 50%,#8a6a52 70%,#4a3a2c 100%)">
    <div class="badge"><span><svg width="18" height="18" viewBox="0 0 22 22"><path d="M8 1h6v7h7v6h-7v7H8v-7H1V8h7z" fill="#000"/></svg>134</span></div>
  </div>

  <div class="project-label">Project Name Here</div>
  <div class="project-label">Project Name Here</div>
  <div class="project-label">Project Name Here</div>

  <div class="project-photo" role="img" aria-label="Project photo: boy with a guitar at a tent" style="background:linear-gradient(120deg,#15110e 0,#3a2d22 45%,#6e5640 80%,#8a7052 100%)">
    <div class="badge"><span><svg width="18" height="18" viewBox="0 0 22 22"><path d="M8 1h6v7h7v6h-7v7H8v-7H1V8h7z" fill="#000"/></svg>134</span></div>
  </div>
  <div class="project-photo" role="img" aria-label="Project photo: two little girls walking on grass" style="background:linear-gradient(180deg,#7a9a58 0,#4d6d30 45%,#3a5522 70%,#6a8a44 100%)">
    <div class="badge"><span><svg width="18" height="18" viewBox="0 0 22 22"><path d="M8 1h6v7h7v6h-7v7H8v-7H1V8h7z" fill="#000"/></svg>134</span></div>
  </div>
  <div class="project-photo" role="img" aria-label="Project photo: friends lying together on the grass" style="background:linear-gradient(135deg,#5a2a1c 0,#a8705a 40%,#d8b8a6 70%,#efe6de 100%)">
    <div class="badge"><span><svg width="18" height="18" viewBox="0 0 22 22"><path d="M8 1h6v7h7v6h-7v7H8v-7H1V8h7z" fill="#000"/></svg>134</span></div>
  </div>
</main>

</body>
</html>
```